Gourmet food company looking for a dazzling label for their premuim vinagrette dressings

Need a food label that will dazzle our customer and prove what a premium product we have. We make high end gourmet dressing for vegetables, fruit, meat, poultry and fish.

Our label will fit on a 250 mil Tolvenka Square bottle. Labels should be a 4x5 or even 5x5 depending on the design. Nutritionals, bar codes and company blurb will be supplied later. We really want to test you all's talent on this one and are very excited to see your renderings!

Our dressings are Champagne Pear Vinaigrette, White Balsmic Vinaigrette, Mojito Lime Vinaigrette, Creamy-Avacado Lime Vinaigrette, and Asian Sesame Vinaigrette. I hope these names will help you envision our product and kinda what we are looking for.
Updates

Thank you all so far for your renderings.I really don't want pictures if that helps. Our logo can be smaller and/or the name of the product bigger. Perhaps we can even redesign Velora and remove the leaf as I don't really care for what I see yet.So good luck and thanks Added Friday, August 19, 2016

I am still looking for that clean - elegant design for our product as our product is just that. If you look on the internet at vinegars and oils you will see many designs that are simple yet elegant. Creative lettering, bordering, color (can be black and white) and size will help accomplish this. So I invite you to use all your creativity and help me find just what we need.Many thanks Added Tuesday, August 23, 2016

Project Deadline Extended Reason: So many great designs coming in that I wanted a few extra days to tweek!Great job all Added Friday, August 26, 2016

Project Deadline Extended Reason: Very good designs thus far. We just need a few more days.Thanks Added Wednesday, August 31, 2016

Target Market(s)

High end grocery and specialty stores.

Our side panel on the label will say "At Velora we're fanatics for great flavors and are passionate about finding the best ingredients. From simple to elegant our products are "simply velora".

Industry/Entity Type

It Company

Font styles to use
Serif
Decorative
Script

Requirements
Must have
• A label that will draw the consumer to pick it up! Need something bold and elegant...
Nice to have
• Again, I really would like to have a label that pops. Since the bottle front is only about 2inches in width it will need some creativity. Would like something very simple and elegant.
• If the designer does not like the logo, please feel free to design without it!
Should not have
• Dark dark colors. We are selling dressing and we don't want any colors that may distort the contents.
• No stock photos for the front. I don't want our dressing to look like the others on the self. Brambleth Kitchen just uses lettering and a their packaging is eye catching

```html
<!DOCTYPE html>
<html lang="en">
<head>
<meta charset="utf-8">
<title>Velora White Balsmic Vinaigrette Label</title>
<link href="https://fonts.googleapis.com/css2?family=Cinzel:wght@400;500&display=swap" rel="stylesheet">
<style>
  :root {
    --page: #ffffff;
    --label-yellow: #e8c41c;
    --label-light: #f3dc6a;
    --ink-white: #ffffff;
    --ink-dark: #3b3110;
  }
  html, body {
    margin: 0;
    padding: 0;
    width: 1200px;
    height: 1200px;
    overflow: hidden;
    background: var(--page);
  }
  .canvas {
    position: relative;
    width: 1200px;
    height: 1200px;
    background: var(--page);
  }
  .label {
    position: absolute;
    left: 410px;
    top: 60px;
    width: 380px;
    height: 1080px;
    background: var(--label-yellow);
    border-radius: 18px;
    font-family: "Cinzel", "Times New Roman", serif;
    text-align: center;
  }
  .drip-artwork {
    position: absolute;
    left: 150px;
    top: 0;
    width: 80px;
    height: 560px;
    border-radius: 0 0 40px 40px;
    background: linear-gradient(180deg, var(--label-yellow) 0%, var(--label-light) 100%);
  }
  .brand {
    position: absolute;
    left: 0;
    right: 0;
    top: 740px;
    margin: 0;
    font-size: 34px;
    font-weight: 500;
    color: var(--ink-dark);
    letter-spacing: 1px;
    line-height: 1;
  }
  .brand-tagline {
    position: absolute;
    left: 0;
    right: 0;
    top: 777px;
    margin: 0;
    font-size: 6px;
    font-weight: 500;
    letter-spacing: 1.5px;
    color: var(--ink-dark);
    line-height: 1;
  }
  .product-name {
    position: absolute;
    left: 0;
    right: 0;
    top: 797px;
    margin: 0;
    font-size: 62px;
    font-weight: 400;
    color: var(--ink-white);
    line-height: 60px;
    letter-spacing: 1px;
  }
  .product-type {
    position: absolute;
    left: 0;
    right: 0;
    top: 924px;
    margin: 0;
    font-size: 26px;
    color: var(--ink-white);
    letter-spacing: 1px;
    line-height: 1;
  }
  .volume {
    position: absolute;
    left: 0;
    right: 0;
    top: 980px;
    margin: 0;
    font-size: 20px;
    color: var(--ink-white);
    line-height: 1;
  }
</style>
</head>
<body>
<main class="canvas">
  <section class="label">
    <div class="drip-artwork" role="img" aria-label="Illustration of a thin white line of dressing falling from the top edge and ending in a single droplet"></div>
    <h2 class="brand">Velora</h2>
    <p class="brand-tagline">WONDERFULLY RICH DRESSING</p>
    <h1 class="product-name">WHITE<br>BALSMIC</h1>
    <p class="product-type">VINAIGRETTE</p>
    <p class="volume">250 ML</p>
  </section>
</main>
</body>
</html>
```